Engineering Consultant Business Card

I'm starting a new business as a high-end engineering consultant in a niche field. I've attached the jpg for my logo plus the branding guideline document that I've been following. You can see my business website here: www.tarvikworks.com
I'd like a business card that has the logo on one side, then the other side has (in any order): Tarvik Works, Inc.
Dana Whitlock
President and Chief EMC Engineer
www.tarvikworks.com
dana@tarvikworks.com
Optional: motto "We will solve your EMC problems as early as possible—ideally before they even start."
I'm not planning on including a phone number
Target Market(s)
Businesses, especially makers of electronics hardware
Industry/Entity Type
Electrical engineering
Contact Information for Business Card
Company name, my name, website, email

```html
<!DOCTYPE html>
<html lang="en">
<head>
<meta charset="utf-8">
<title>Tarvik Works, Inc. — Business Card</title>
<link rel="stylesheet" href="https://fonts.googleapis.com/css2?family=Roboto+Condensed:wght@400;700&display=swap">
<style>
  :root {
    --page-bg: #e6e8ee;
    --card-blue: #27317a;
    --card-blue-light: #56629f;
    --card-blue-deep: #1c2466;
    --card-dark: #141418;
    --card-dark-edge: #2b2b2e;
    --text-white: #ffffff;
    --text-soft: #d7dbef;
    --text-muted: #b9bfdc;
    --accent-bar: #e9ecf7;
  }
  * { margin: 0; padding: 0; box-sizing: border-box; }
  html, body {
    width: 1200px;
    height: 780px;
    overflow: hidden;
    background: var(--page-bg);
  }
  .canvas {
    position: relative;
    width: 1200px;
    height: 780px;
  }
  .business-card {
    position: absolute;
    left: 40px;
    top: 81px;
    width: 1120px;
    height: 618px;
    overflow: hidden;
    background:
      radial-gradient(ellipse 420px 360px at 240px 260px, var(--card-blue-light) 0%, rgba(86,98,159,0) 100%),
      linear-gradient(90deg, var(--card-blue) 0%, var(--card-blue-deep) 60%, var(--card-blue-deep) 100%);
    font-family: "Roboto Condensed", sans-serif;
    box-shadow: 0 18px 40px rgba(20, 24, 50, 0.25);
  }
  .decor-panel {
    position: absolute;
    right: 0;
    top: 0;
    width: 630px;
    height: 618px;
  }
  .brand-lockup {
    position: absolute;
    left: 36px;
    top: 92px;
    display: flex;
    align-items: center;
    gap: 20px;
  }
  .brand-dot {
    width: 64px;
    height: 64px;
    border-radius: 50%;
    background: var(--text-white);
  }
  .brand-name {
    font-size: 64px;
    font-weight: 700;
    color: var(--text-white);
    line-height: 1;
  }
  .name-bar {
    position: absolute;
    left: 0;
    top: 281px;
    width: 32px;
    height: 94px;
    background: var(--accent-bar);
  }
  .person-name {
    position: absolute;
    left: 42px;
    top: 282px;
    font-size: 56px;
    font-weight: 700;
    color: var(--text-soft);
    line-height: 1;
  }
  .person-title {
    position: absolute;
    left: 42px;
    top: 344px;
    font-size: 27px;
    font-weight: 400;
    color: var(--text-muted);
    line-height: 1;
  }
  .contact-list {
    position: absolute;
    left: 42px;
    top: 414px;
    list-style: none;
  }
  .contact-item {
    display: flex;
    align-items: center;
    gap: 17px;
    height: 37px;
    font-size: 25px;
    color: var(--text-muted);
  }
  .contact-icon { width: 25px; height: 25px; flex: none; }
  .motto {
    position: absolute;
    left: 42px;
    top: 512px;
    width: 520px;
    font-size: 25px;
    line-height: 34px;
    color: var(--text-muted);
  }
</style>
</head>
<body>
<main class="canvas">
  <section class="business-card" aria-label="Tarvik Works, Inc. business card">
    <svg class="decor-panel" viewBox="0 0 630 618" role="img" aria-label="Large dark brand decoration area">
      <defs>
        <radialGradient id="decorFade" cx="0.62" cy="0.5" r="0.6">
          <stop offset="0" stop-color="#0e0e12"/>
          <stop offset="0.7" stop-color="#141418"/>
          <stop offset="1" stop-color="#1c2466" stop-opacity="0"/>
        </radialGradient>
      </defs>
      <rect width="630" height="618" fill="url(#decorFade)"/>
    </svg>

    <div class="brand-lockup">
      <span class="brand-dot" aria-hidden="true"></span>
      <span class="brand-name">Tarvik Works</span>
    </div>

    <span class="name-bar" aria-hidden="true"></span>
    <h1 class="person-name">Dana Whitlock</h1>
    <p class="person-title">President and Chief EMC Engineer</p>

    <ul class="contact-list">
      <li class="contact-item">
        <svg class="contact-icon" viewBox="0 0 24 24" aria-hidden="true">
          <circle cx="12" cy="12" r="10" fill="none" stroke="#b9bfdc" stroke-width="2"/>
          <ellipse cx="12" cy="12" rx="4.5" ry="10" fill="none" stroke="#b9bfdc" stroke-width="1.6"/>
          <line x1="2" y1="12" x2="22" y2="12" stroke="#b9bfdc" stroke-width="1.6"/>
        </svg>
        <span>www.tarvikworks.com</span>
      </li>
      <li class="contact-item">
        <svg class="contact-icon" viewBox="0 0 24 24" aria-hidden="true">
          <rect x="2" y="6" width="20" height="14" rx="1.5" fill="none" stroke="#b9bfdc" stroke-width="2"/>
          <polyline points="2,7 12,14 22,7" fill="none" stroke="#b9bfdc" stroke-width="1.8"/>
        </svg>
        <span>dana@tarvikworks.com</span>
      </li>
    </ul>

    <p class="motto">We will solve your EMC problems as early as possible —ideally before they even start</p>
  </section>
</main>
</body>
</html>
```